International Travel Technology R&D business needs a wordpress website

We are a start up team of initially 2 individuals but plan to grow our team quickly, we have deep experience in travel technology. Our goal is to provide next generation technology research and development on behalf of our clients who are leading players in the travel technology industry. Attached our logos.

Target Market(s)

Travel Technology companies

Industry/Entity Type

Travel Industry

Coding

Coded - Design and coding required

Font styles to use
Sans Serif

Requirements
Must have
• Make use of our logo and colour scheme in the attached. Has to have a sense of adventure/ stepping into the unknown but equally must convey a sense of professionalism , we are a safe pair of hands. Sample themes are in the attachment .
Nice to have
• We have identified a theme on layoutbazaar which we feel would be inspirational. We hahe attached them to help in the design as inspiration.
Should not have
• images of airplanes , hotels etc, we want to project a future image.

```html
<!DOCTYPE html>
<html lang="en">
<head>
<meta charset="utf-8">
<title>Voyara Labs — Generation Technology Research</title>
<link href="https://fonts.googleapis.com/css2?family=Raleway:wght@400;500;600;700;800&family=Open+Sans:wght@400;600&display=swap" rel="stylesheet">
<style>
:root{
  --navy:#253a7e;
  --navy-deep:#1f3170;
  --green:#6aa842;
  --green-dark:#5a9436;
  --ink:#333;
  --muted:#8a8a8a;
  --line:#e3e3e3;
  --pale:#f4f4f4;
  --footer:#2b2b2b;
  --footer-deep:#1f1f1f;
  --white:#fff;
}
*{box-sizing:border-box;margin:0;padding:0}
html,body{width:1200px;height:3120px;overflow:hidden}
body{font-family:"Raleway",sans-serif;color:var(--ink);background:var(--white);font-size:14px}
.wrap{width:1004px;margin:0 auto;position:relative}

/* header */
.site-header{height:135px}
.site-header .wrap{display:flex;align-items:center;height:135px}
.brand{display:flex;align-items:center;gap:10px;font-weight:800;font-size:30px;color:var(--navy);letter-spacing:1px}
.brand-dot{width:18px;height:18px;border-radius:50%;background:var(--green)}
.contact-bits{margin-left:auto;display:flex;gap:60px}
.contact-bit{display:flex;gap:14px;align-items:flex-start}
.contact-bit small{display:block;font-size:12px;color:var(--ink);margin-bottom:6px}
.contact-bit span{color:var(--green);font-size:14px;line-height:1.35}
/* nav */
.main-nav{background:var(--navy);height:55px}
.main-nav ul{display:flex;list-style:none;height:55px;width:1004px;margin:0 auto}
.main-nav li{flex:1;display:flex;align-items:center;justify-content:center;color:var(--white);font-size:12px;font-weight:600;letter-spacing:.3px}
.main-nav li.active{background:var(--green);flex:0 0 134px}
/* hero */
.hero{height:490px;position:relative;background:linear-gradient(180deg,#3d8fd8 0%,#7ebbea 45%,#b9d9ef 60%,#7c9a3c 72%,#b89a3a 100%)}
.hero-text{position:absolute;left:98px;top:105px;color:var(--white)}
.hero-text h2{font-weight:500;font-size:28px;letter-spacing:.5px}
.hero-text h1{font-weight:800;font-size:50px;margin-top:10px;letter-spacing:.5px}
.hero-text p{font-size:16px;line-height:1.6;margin-top:10px;width:360px}
.dots{display:flex;gap:12px;margin-top:36px}
.dots i{width:14px;height:14px;border-radius:50%;background:rgba(255,255,255,.85)}
.dots i:first-child{background:var(--navy)}
.hero-photo{position:absolute;left:460px;top:30px;width:690px;height:440px;background:radial-gradient(ellipse at 50% 60%,rgba(40,150,140,.55),rgba(255,255,255,0) 70%)}
/* welcome */
.welcome{display:flex;height:355px}
.welcome-photo{width:600px;background:linear-gradient(160deg,#4c5fa0 0%,#2e3f7d 55%,#1e2a55 100%)}
.welcome-copy{flex:1;background:var(--green);color:var(--white);padding:40px 50px 0 48px}
.welcome-copy h3{font-weight:500;font-size:26px;margin-bottom:18px}
.welcome-copy p{font-size:12.5px;line-height:1.85;margin-bottom:12px}
.btn{display:inline-block;font-size:11px;font-weight:700;color:var(--white);text-align:center;letter-spacing:.3px}
.btn-navy{background:var(--navy);padding:13px 30px;margin-top:10px}
/* services */
.services{background:var(--pale);height:480px;padding-top:52px}
.section-title{text-align:center;font-weight:500;font-size:26px;color:var(--ink)}
.service-grid{display:flex;margin-top:44px;border:1px solid var(--line);background:var(--white)}
.service{flex:1;text-align:center;padding:24px 30px 28px;border-right:1px solid var(--line)}
.service:last-child{border-right:none}
.service-icon{width:104px;height:104px;border-radius:50%;margin:0 auto;display:flex;align-items:center;justify-content:center}
.service-icon.green{background:var(--green)}
.service-icon.navy{background:var(--navy)}
.service h4{font-size:14px;font-weight:700;margin-top:22px}
.service p{font-size:12px;color:var(--muted);line-height:1.7;margin-top:8px}
.service .btn{width:130px;padding:12px 0;margin-top:20px}
.btn-green{background:var(--green)}
/* projects */
.projects{height:485px;padding-top:50px}
.section-lead{text-align:center;font-size:13px;color:#555;line-height:1.75;width:640px;margin:12px auto 0}
.project-grid{display:flex;justify-content:space-between;margin-top:18px}
.project{width:316px;text-align:center}
.project-photo{height:200px}
.project h5{font-size:14px;font-weight:600;line-height:1.6;margin-top:18px}
.project hr{width:126px;border:none;border-top:2px solid #bbb;margin:10px auto 0}
/* feedback */
.feedback{height:382px;background:linear-gradient(180deg,var(--navy) 0%,var(--navy-deep) 100%);padding-top:60px;color:var(--white)}
.feedback .section-title{color:var(--white)}
.testimonials{display:flex;justify-content:space-between;margin-top:40px}
.testimonial{width:490px}
.testimonial-top{display:flex;gap:22px}
.avatar{width:116px;height:116px;border-radius:50%;border:4px solid var(--green);flex:none}
.quote-mark{color:var(--green);font-size:46px;font-weight:800;line-height:.8;font-family:Georgia,serif}
.testimonial-head{display:flex;gap:10px}
.testimonial-head h6{font-size:15px;font-weight:500}
.testimonial-head .who{font-size:12px;margin-top:12px;font-weight:700}
.testimonial-head .who em{font-style:normal;font-weight:400;opacity:.8}
.stars{display:flex;gap:4px;margin-top:10px}
.testimonial blockquote{font-style:italic;font-size:12.5px;line-height:1.75;margin-top:18px}
/* callback */
.callback{height:456px;position:relative}
.callback-form{position:absolute;left:98px;top:48px;width:484px}
.callback-form h3{font-weight:500;font-size:26px;margin-bottom:22px}
.field{height:44px;border:1px solid var(--line);background:#fafafa;margin-bottom:8px;display:flex;align-items:center;padding:0 16px;font-size:12px;color:#777;justify-content:space-between}
.field.message{height:88px;align-items:flex-start;padding-top:14px}
.field i{width:9px;height:9px;background:#ddd;border-radius:2px}
.callback-form .btn{width:100%;padding:14px 0;margin-top:4px}
.callback-photo{position:absolute;left:700px;top:48px;width:410px;height:408px;background:radial-gradient(ellipse at 55% 55%,#7fa2c9 0%,#c9d7e6 55%,rgba(255,255,255,0) 75%)}
/* footer */
.site-footer{background:var(--footer);height:232px;color:#bbb}
.site-footer .wrap{display:flex;padding-top:38px}
.footer-col h6{color:var(--white);font-size:15px;font-weight:500;margin-bottom:12px}
.footer-brand{width:316px}
.footer-brand .brand{color:var(--white);font-size:26px}
.footer-brand p{font-size:12px;line-height:1.6;margin-top:14px;color:#9a9a9a;width:250px}
.socials{display:flex;gap:10px;margin-top:14px}
.socials i{width:30px;height:30px;border-radius:50%;background:#3c3c3c}
.quick-links{width:158px}
.quick-links ul{list-style:none;font-size:11px;line-height:1.7}
.newsletter{width:314px}
.newsletter p{font-size:12px;line-height:1.5;width:250px}
.newsletter .field{background:#3a3a3a;border-color:#4a4a4a;width:242px;height:38px;margin-top:12px;color:#999}
.newsletter .btn{padding:10px 16px;margin-top:6px}
.contact-list{font-size:12px;line-height:1.6}
.contact-list div{display:flex;gap:10px;margin-bottom:12px}
.footer-bottom{background:var(--footer-deep);height:50px;color:#bbb;font-size:12px;display:flex;align-items:center}
.footer-bottom .wrap{display:flex;justify-content:center}
</style>
</head>
<body>

<header class="site-header">
  <div class="wrap">
    <div class="brand"><span class="brand-dot"></span>VOYARA LABS</div>
    <div class="contact-bits">
      <div class="contact-bit">
        <svg width="22" height="36" viewBox="0 0 22 36"><rect x="2" y="2" width="18" height="32" rx="3" fill="none" stroke="#333" stroke-width="3"/><rect x="8" y="28" width="6" height="2" fill="#333"/></svg>
        <div><small>Phone:</small><span>(+100) 555-0142</span></div>
      </div>
      <div class="contact-bit">
        <svg width="26" height="36" viewBox="0 0 26 36"><path d="M13 1C6 1 1 6 1 13c0 9 12 22 12 22s12-13 12-22C25 6 20 1 13 1z" fill="#333"/><circle cx="13" cy="13" r="5" fill="#fff"/></svg>
        <div><small>Location:</small><span>48 Meridian Row,<br>Northgate 2207</span></div>
      </div>
    </div>
  </div>
</header>

<nav class="main-nav">
  <ul>
    <li class="active">HOME</li><li>ABOUT US</li><li>SERVICES</li><li>PROJECTS</li><li>PORTFOLIO</li><li>LATEST NEWS</li><li>CONTACT US</li>
  </ul>
</nav>

<section class="hero">
  <div class="hero-photo" role="img" aria-label="Group of friends leaping beside a teal camper van on a sunny hillside road"></div>
  <div class="hero-text">
    <h2>GENERATION TECHNOLOGY</h2>
    <h1>RESEARCH</h1>
    <p>Nam libero tempore, cum soluta nobis est eligendi optio cumque nihil imped...</p>
    <div class="dots"><i></i><i></i><i></i></div>
  </div>
</section>

<section class="welcome">
  <div class="welcome-photo" role="img" aria-label="Traveller with raised arms in an open car on a winding coastal road at dusk"></div>
  <div class="welcome-copy">
    <h3>Welcome to Voyara Labs</h3>
    <p>Nam libero tempore, cum soluta nobis est eligendi optio cumque nihil impediters quo minus id quod maxime placeat facere possimus, omnis voluptas assumenda est, omnis dolor repellendus. Temporibus autem quibusdam...</p>
    <p>Debitis aut rerum necessitatibus saepe eveniet ut et voluptates repudiandae sint et molestiae non recusandae. Itaque earum rerum hic tenetur a sapiente delectus, ut aut reiciendis aut officiis...</p>
    <span class="btn btn-navy">LEARN MORE</span>
  </div>
</section>

<section class="services">
  <div class="wrap">
    <h2 class="section-title">Our Featured Services</h2>
    <div class="service-grid">
      <div class="service">
        <div class="service-icon green">
          <svg width="52" height="40" viewBox="0 0 52 40"><path d="M10 16l5-11h22l5 11h4v14h-4v6h-7v-6H17v6h-7v-6H6V16z" fill="#fff"/><circle cx="14" cy="23" r="3" fill="#6aa842"/><circle cx="38" cy="23" r="3" fill="#6aa842"/><rect x="16" y="9" width="20" height="7" fill="#6aa842"/></svg>
        </div>
        <h4>Deserunt mollitiacum</h4>
        <p>Nam libero tempore, cum soluta nobis est eligen optio cumque nihil impedit quo...</p>
        <span class="btn btn-green">LEARN MORE</span>
      </div>
      <div class="service">
        <div class="service-icon navy">
          <svg width="48" height="48" viewBox="0 0 48 48"><circle cx="24" cy="24" r="21" fill="#fff"/><path d="M12 12c5 2 6 6 10 7s3 6 0 8-2 8-6 10c-2-5-6-8-5-13s-3-6 1-12zM30 8c4 3 2 6 6 8s5 6 3 10c-3-1-6 0-8-3s-5-5-1-15z" fill="#253a7e"/></svg>
        </div>
        <h4>Deserunt mollitiacum</h4>
        <p>Nam libero tempore, cum soluta nobis est eligen optio cumque nihil impedit quo...</p>
        <span class="btn btn-navy" style="margin-top:20px;padding:12px 0">LEARN MORE</span>
      </div>
      <div class="service">
        <div class="service-icon navy">
          <svg width="48" height="44" viewBox="0 0 48 44"><path d="M46 2L2 20l12 5 4 16 7-10 12 8z" fill="#fff"/><path d="M14 25L46 2 20 29z" fill="#c9d0e6"/></svg>
        </div>
        <h4>Deserunt mollitiacum</h4>
        <p>Nam libero tempore, cum soluta nobis est eligen optio cumque nihil impedit quo...</p>
        <span class="btn btn-navy" style="margin-top:20px;padding:12px 0">LEARN MORE</span>
      </div>
    </div>
  </div>
</section>

<section class="projects">
  <div class="wrap">
    <h2 class="section-title">Projects</h2>
    <p class="section-lead">Nam libero tempore, cum soluta nobis est eligendi optio cumque nihil impedit quo minus id quod maxime placeat facere possimus, omnis voluptas assumenda.</p>
    <div class="project-grid">
      <div class="project">
        <div class="project-photo" role="img" aria-label="Team gathered around a laptop in a bright office" style="background:linear-gradient(160deg,#c9dcea,#6f8fae 60%,#44566c)"></div>
        <h5>Maxime placeat facere possimus<br>Deserunt mollitia animi</h5><hr>
      </div>
      <div class="project">
        <div class="project-photo" role="img" aria-label="Woman working at a desk with a computer" style="background:linear-gradient(160deg,#e9e4dc,#b7a48c 60%,#3b3a3e)"></div>
        <h5>Maxime placeat facere possimus<br>Deserunt mollitia animi</h5><hr>
      </div>
      <div class="project">
        <div class="project-photo" role="img" aria-label="Colleagues meeting around a table with a laptop" style="background:linear-gradient(160deg,#d6d9dd,#8b9096 60%,#3a3c40)"></div>
        <h5>Maxime placeat facere possimus<br>Deserunt mollitia animi</h5><hr>
      </div>
    </div>
  </div>
</section>

<section class="feedback">
  <div class="wrap">
    <h2 class="section-title">Feedback From Our Clients</h2>
    <div class="testimonials">
      <article class="testimonial">
        <div class="testimonial-top">
          <div class="avatar" role="img" aria-label="Portrait of client" style="background:linear-gradient(160deg,#e8d2bf,#9c7a62)"></div>
          <div class="testimonial-head">
            <span class="quote-mark">“</span>
            <div>
              <h6>Voyara Labs Feedback</h6>
              <div class="who">Daniel Roswell <em>/ CEO</em></div>
              <div class="stars">
                <svg width="92" height="16" viewBox="0 0 92 16"><g fill="#6aa842"><path id="st" d="M8 1l2.1 4.5 4.9.5-3.7 3.3 1.1 4.8L8 11.6 3.6 14.1l1.1-4.8L1 6l4.9-.5z"/><use href="#st" x="19"/><use href="#st" x="38"/><use href="#st" x="57"/></g><use href="#st" x="76" fill="none" stroke="#6aa842"/></svg>
              </div>
            </div>
          </div>
        </div>
        <blockquote>"similique sunt in culpa qui officia deserunt mollitia animi, id est laborum et dol orum fuga. Et harum quidem rerum facilis est et expedita distinctio"</blockquote>
      </article>
      <article class="testimonial">
        <div class="testimonial-top">
          <div class="avatar" role="img" aria-label="Portrait of client" style="background:linear-gradient(160deg,#ead7c6,#7a5a48)"></div>
          <div class="testimonial-head">
            <span class="quote-mark">“</span>
            <div>
              <h6>Voyara Labs Feedback</h6>
              <div class="who">Daniel Roswell <em>/ CEO</em></div>
              <div class="stars">
                <svg width="92" height="16" viewBox="0 0 92 16"><g fill="#6aa842"><use href="#st"/><use href="#st" x="19"/><use href="#st" x="38"/><use href="#st" x="57"/></g><use href="#st" x="76" fill="none" stroke="#6aa842"/></svg>
              </div>
            </div>
          </div>
        </div>
        <blockquote>"similique sunt in culpa qui officia deserunt mollitia animi, id est laborum et dol orum fuga. Et harum quidem rerum facilis est et expedita distinctio"</blockquote>
      </article>
    </div>
  </div>
</section>

<section class="callback">
  <form class="callback-form">
    <h3>Request a Call Back</h3>
    <div class="field">Your name...<i></i></div>
    <div class="field">Your E-mail<i></i></div>
    <div class="field">Your Phone number<i></i></div>
    <div class="field message">Type Message</div>
    <span class="btn btn-green">CLICK TO SEND REQUEST</span>
  </form>
  <div class="callback-photo" role="img" aria-label="Smiling man in a denim shirt holding an open laptop"></div>
</section>

<footer class="site-footer">
  <div class="wrap">
    <div class="footer-col footer-brand">
      <div class="brand"><span class="brand-dot"></span>VOYARA LABS</div>
      <p>Cum soluta nobis est eligendi optio cumque nihil impedit quo minus id quod maxime pla ceat facere possimus, omni voluptas...</p>
      <div class="socials"><i></i><i></i><i></i><i></i></div>
    </div>
    <div class="footer-col quick-links">
      <h6>Quick Links</h6>
      <ul><li>HOME</li><li>ABOUT US</li><li>SERVICES</li><li>PROJECTS</li><li>PORTFOLIO</li><li>LATEST NEWS</li><li>CONTACT US</li></ul>
    </div>
    <div class="footer-col newsletter">
      <h6>Newsletter Subscription</h6>
      <p>Register Your email address to get inform about us</p>
      <div class="field">Email Address</div>
      <span class="btn btn-green">SUBSCRIBE</span>
    </div>
    <div class="footer-col">
      <h6>Contact Us</h6>
      <div class="contact-list">
        <div><svg width="10" height="14" viewBox="0 0 26 36"><path d="M13 1C6 1 1 6 1 13c0 9 12 22 12 22s12-13 12-22C25 6 20 1 13 1z" fill="#999"/></svg><span>Halden Brook &amp; Partners<br>220 Orchard Lane Suite 14<br>Westmere, QL 40712</span></div>
        <div><svg width="10" height="14" viewBox="0 0 22 36"><rect x="2" y="2" width="18" height="32" rx="3" fill="#999"/></svg><span>+100-555-0142</span></div>
        <div><svg width="12" height="10" viewBox="0 0 12 10"><rect width="12" height="10" fill="#999"/><path d="M0 0l6 5 6-5" stroke="#2b2b2b" fill="none"/></svg><span>hello@voyaralabs.example</span></div>
      </div>
    </div>
  </div>
</footer>
<div class="footer-bottom"><div class="wrap">Copyright © 2016, Voyara Labs. All Rights Reserved.</div></div>

</body>
</html>
```